Real Estate Company Looking for Business Card Designs for 3 Executives

Hello!
Thanks so much for considering our project! We are a real estate investment company located in Edmonton, Alberta called Marlbeck Group of Companies. We invest/develop both commercial and residential real estate and are looking to create 3 DOUBLE-SIDED business cards for 3 top executives in the company! (for some reason it won't let us select the double-sided option, but yes, the cards are double sided and would be happy to tip extra)

We have certain guidelines that we want our business cards to for sure follow - the back of the Business card has to be the Black Background Version of the Logo which has already been designed and linked as a file (first file). We want the entire back of the card to simply just be the black background logo. In terms of the front of the card, would like to see a smaller version of the white background logo (linked as the second file) in the top left hand corner - of course, feel free to get creative and we can make revisions together along the way! and Then after that, just text. We want the card to be sharp, clean, easy on the eyes and highly professional looking. We would like the card to include the Full name of the Company (Marlbeck Group of Companies), Name of the Person, Title, Phone, Email. If possible please provide the front part of the card for 3 people:

1) Marlbeck Group of Companies, Lena Okafor, Chief Financial Officer, 780-555-0162, lenaokafor@marlbeckgroup.example

2) Marlbeck Group of Companies, Tobias Okafor, Chief Executive Officer, 780-555-0148, tobiasokafor@marlbeckgroup.example

3) Marlbeck Group of Companies, Rui Dalton, Chief Operations Officer, 587-555-0193, ruidalton@marlbeckgroup.example

Thank you so much for considering our project & we look forward to seeing your designs!

```html
<!DOCTYPE html>
<html lang="en">
<head>
<meta charset="utf-8">
<title>Marlbeck Business Cards – Executive Fronts and Back</title>
<link rel="stylesheet" href="https://fonts.googleapis.com/css2?family=Arimo:wght@400;700&family=Josefin+Sans:wght@400&display=swap">
<style>
  :root {
    --backdrop: #e4e4e2;
    --card: #2f2f2f;
    --ink: #ffffff;
    --ink-soft: #e6e6e6;
    --rule: #bdbdbd;
  }
  * { margin: 0; padding: 0; box-sizing: border-box; }
  html, body {
    width: 1200px;
    height: 801px;
    overflow: hidden;
    background: var(--backdrop);
  }
  .canvas {
    width: 1200px;
    height: 801px;
    display: grid;
    grid-template-columns: repeat(2, 540px);
    grid-template-rows: repeat(2, 308px);
    gap: 40px 40px;
    justify-content: center;
    align-content: center;
  }
  .card {
    position: relative;
    width: 540px;
    height: 308px;
    background: var(--card);
    box-shadow: 0 10px 24px rgba(0,0,0,0.22);
    color: var(--ink);
    overflow: hidden;
  }

  /* Brand lockup */
  .brand-mark {
    position: absolute;
    left: 0;
    right: 0;
    top: 56px;
    display: flex;
    flex-direction: column;
    align-items: center;
    gap: 10px;
  }
  .brand-mark__row {
    display: flex;
    align-items: center;
    gap: 12px;
  }
  .brand-mark__square {
    width: 22px;
    height: 22px;
    background: var(--ink);
  }
  .brand-mark__name {
    font-family: "Josefin Sans", sans-serif;
    font-weight: 400;
    font-size: 30px;
    letter-spacing: 8px;
    color: var(--ink);
    white-space: nowrap;
  }
  .brand-mark__company {
    font-family: "Josefin Sans", sans-serif;
    font-size: 12px;
    letter-spacing: 4px;
    text-transform: uppercase;
    color: var(--ink-soft);
    white-space: nowrap;
  }

  /* Front details */
  .details {
    position: absolute;
    left: 0;
    right: 0;
    top: 184px;
    display: flex;
    justify-content: center;
    align-items: center;
  }
  .person {
    text-align: right;
    padding-right: 18px;
    white-space: nowrap;
  }
  .person__name {
    font-family: "Arimo", sans-serif;
    font-weight: 700;
    font-size: 17px;
    letter-spacing: 0.5px;
    text-transform: uppercase;
  }
  .person__title {
    font-family: "Arimo", sans-serif;
    font-size: 13px;
    color: var(--ink-soft);
    margin-top: 4px;
  }
  .divider {
    width: 1px;
    height: 54px;
    background: var(--rule);
    flex: none;
  }
  .contact {
    list-style: none;
    padding-left: 18px;
    font-family: "Arimo", sans-serif;
    font-size: 14px;
    color: var(--ink-soft);
    white-space: nowrap;
  }
  .contact__item {
    display: flex;
    align-items: center;
    gap: 9px;
    line-height: 25px;
  }
  .contact__icon { width: 12px; height: 12px; flex: none; }

  /* Back */
  .pattern-field {
    position: absolute;
    inset: 0;
    background: linear-gradient(135deg, #3a3a3a 0%, #1f1f1f 45%, #363636 70%, #1c1c1c 100%);
  }
  .card--back .brand-mark { top: 118px; }
</style>
</head>
<body>
  <main class="canvas">
    <section class="card card--front" aria-label="Card front, Lena Okafor">
      <div class="brand-mark">
        <div class="brand-mark__row"><span class="brand-mark__square"></span><span class="brand-mark__name">MARLBECK</span></div>
        <p class="brand-mark__company">Marlbeck Group of Companies</p>
      </div>
      <div class="details">
        <div class="person">
          <p class="person__name">Lena Okafor</p>
          <p class="person__title">Chief Financial Officer</p>
        </div>
        <span class="divider"></span>
        <ul class="contact">
          <li class="contact__item">
            <svg class="contact__icon" viewBox="0 0 24 24" aria-hidden="true"><path fill="#e6e6e6" d="M6.6 10.8a15.2 15.2 0 0 0 6.6 6.6l2.2-2.2c.3-.3.7-.4 1-.2 1.1.4 2.3.6 3.6.6.6 0 1 .4 1 1V20c0 .6-.4 1-1 1A17 17 0 0 1 3 4c0-.6.4-1 1-1h3.5c.6 0 1 .4 1 1 0 1.3.2 2.5.6 3.6.1.3 0 .7-.2 1z"/></svg>
            <span>780-555-0162</span>
          </li>
          <li class="contact__item">
            <svg class="contact__icon" viewBox="0 0 24 24" aria-hidden="true"><rect x="2.5" y="5" width="19" height="14" rx="1.5" fill="none" stroke="#e6e6e6" stroke-width="2"/><path d="M3 6l9 7 9-7" fill="none" stroke="#e6e6e6" stroke-width="2"/></svg>
            <span>lenaokafor@marlbeckgroup.example</span>
          </li>
        </ul>
      </div>
    </section>

    <section class="card card--front" aria-label="Card front, Tobias Okafor">
      <div class="brand-mark">
        <div class="brand-mark__row"><span class="brand-mark__square"></span><span class="brand-mark__name">MARLBECK</span></div>
        <p class="brand-mark__company">Marlbeck Group of Companies</p>
      </div>
      <div class="details">
        <div class="person">
          <p class="person__name">Tobias Okafor</p>
          <p class="person__title">Chief Executive Officer</p>
        </div>
        <span class="divider"></span>
        <ul class="contact">
          <li class="contact__item">
            <svg class="contact__icon" viewBox="0 0 24 24" aria-hidden="true"><path fill="#e6e6e6" d="M6.6 10.8a15.2 15.2 0 0 0 6.6 6.6l2.2-2.2c.3-.3.7-.4 1-.2 1.1.4 2.3.6 3.6.6.6 0 1 .4 1 1V20c0 .6-.4 1-1 1A17 17 0 0 1 3 4c0-.6.4-1 1-1h3.5c.6 0 1 .4 1 1 0 1.3.2 2.5.6 3.6.1.3 0 .7-.2 1z"/></svg>
            <span>780-555-0148</span>
          </li>
          <li class="contact__item">
            <svg class="contact__icon" viewBox="0 0 24 24" aria-hidden="true"><rect x="2.5" y="5" width="19" height="14" rx="1.5" fill="none" stroke="#e6e6e6" stroke-width="2"/><path d="M3 6l9 7 9-7" fill="none" stroke="#e6e6e6" stroke-width="2"/></svg>
            <span>tobiasokafor@marlbeckgroup.example</span>
          </li>
        </ul>
      </div>
    </section>

    <section class="card card--front" aria-label="Card front, Rui Dalton">
      <div class="brand-mark">
        <div class="brand-mark__row"><span class="brand-mark__square"></span><span class="brand-mark__name">MARLBECK</span></div>
        <p class="brand-mark__company">Marlbeck Group of Companies</p>
      </div>
      <div class="details">
        <div class="person">
          <p class="person__name">Rui Dalton</p>
          <p class="person__title">Chief Operations Officer</p>
        </div>
        <span class="divider"></span>
        <ul class="contact">
          <li class="contact__item">
            <svg class="contact__icon" viewBox="0 0 24 24" aria-hidden="true"><path fill="#e6e6e6" d="M6.6 10.8a15.2 15.2 0 0 0 6.6 6.6l2.2-2.2c.3-.3.7-.4 1-.2 1.1.4 2.3.6 3.6.6.6 0 1 .4 1 1V20c0 .6-.4 1-1 1A17 17 0 0 1 3 4c0-.6.4-1 1-1h3.5c.6 0 1 .4 1 1 0 1.3.2 2.5.6 3.6.1.3 0 .7-.2 1z"/></svg>
            <span>587-555-0193</span>
          </li>
          <li class="contact__item">
            <svg class="contact__icon" viewBox="0 0 24 24" aria-hidden="true"><rect x="2.5" y="5" width="19" height="14" rx="1.5" fill="none" stroke="#e6e6e6" stroke-width="2"/><path d="M3 6l9 7 9-7" fill="none" stroke="#e6e6e6" stroke-width="2"/></svg>
            <span>ruidalton@marlbeckgroup.example</span>
          </li>
        </ul>
      </div>
    </section>

    <section class="card card--back" aria-label="Card back">
      <div class="pattern-field" role="img" aria-label="Glossy tone-on-tone repeating brand pattern across the card"></div>
      <div class="brand-mark">
        <div class="brand-mark__row"><span class="brand-mark__square"></span><span class="brand-mark__name">MARLBECK</span></div>
        <p class="brand-mark__company">Marlbeck Group of Companies</p>
      </div>
    </section>
  </main>
</body>
</html>
```